Goals Poster 2023 - Poster design of my goals and those that inspire me!

Hi there!
I'm looking to design a visually beautiful poster to represent my goals for 2023
Here is the info:
https://plinkboard.example/app/board/kT7rWqZ2mN4=/?share_link_id=418293057164
You'll see some examples of designs I like within the file too on the right! Notice the neon colours,but open to other suggestions too.,
I think "The year of No" is important.
And the rules down the bottom are particularly important.
Heres an example of a previous year: https://filenook.example/file/d/29KpRtUvWxYz3AbCdEfGhJkLmNoPqRs/view
I want to upgrade the overall design from this.
Thanks!
Ned

```html
<!DOCTYPE html>
<html lang="en">
<head>
<meta charset="utf-8">
<title>The Year of No — Goals 2023</title>
<link href="https://fonts.googleapis.com/css2?family=Poppins:wght@400;500;600;700;800&display=swap" rel="stylesheet">
<style>
:root{
  --ink:#000;
  --card:#1c1c1c;
  --text:#fff;
  --muted:#d8d8d8;
  --orange:#f7931e;
  --orange-deep:#e8541e;
  --green:#5ec72b;
  --green-deep:#3a9a17;
  --purple:#6a1fc9;
}
*{box-sizing:border-box;margin:0;padding:0}
html,body{width:1200px;height:3465px;overflow:hidden;background:var(--ink)}
body{font-family:'Poppins',sans-serif;color:var(--text);position:relative}
.abs{position:absolute}
.hero{left:0;top:0;width:1200px;height:822px;background:#000}
.stage{left:0;top:822px;width:1200px;height:2643px;background:linear-gradient(180deg,#1e1e1e 0%,#121212 40%,#0d0d12 100%)}
.why{top:125px;width:1200px;text-align:center;font-size:35px;font-weight:600;line-height:47px}
.title{top:276px;width:1200px;text-align:center;font-size:100px;font-weight:800;letter-spacing:1px;
  background:linear-gradient(180deg,#ffc23a,#f26a16);-webkit-background-clip:text;background-clip:text;color:transparent}
.bullets{left:108px;top:470px;width:520px;font-size:17px;font-weight:600;line-height:28px;list-style:none}
.bullets li{padding-left:20px;position:relative}
.bullets li::before{content:"";position:absolute;left:2px;top:12px;width:6px;height:6px;border-radius:50%;background:#fff}
.bar{display:flex;align-items:center;justify-content:center;font-weight:600;font-size:23px;border-radius:6px}
.bar-green{left:695px;top:470px;width:408px;height:56px;background:linear-gradient(90deg,var(--green),var(--green-deep))}
.statement{top:547px;width:195px;height:168px;background:#1b1b1b;border-radius:8px;display:flex;align-items:center;justify-content:center;text-align:center;font-size:18px;line-height:29px;color:var(--muted);padding:0 24px}
.illustration{border-radius:14px}
.bar-purple{left:77px;top:890px;width:300px;height:96px;background:linear-gradient(90deg,#4a14a8,var(--purple));font-size:24px;line-height:30px;text-align:center}
.people{left:77px;top:1000px;width:300px;height:1230px;background:#1e1e1e;border-radius:8px}
.person{position:absolute;left:75px;width:150px;text-align:center}
.portrait{width:150px;height:128px;border-radius:12px;background:linear-gradient(160deg,#8a6a55,#3a2e28)}
.person-name{margin-top:18px;color:var(--orange);font-size:19px;font-weight:600;line-height:30px}
.bar-pink{left:820px;top:890px;width:300px;height:56px;background:linear-gradient(90deg,#e0407e,#f464c0);font-size:23px}
.traits{left:820px;top:965px;width:300px;list-style:none;background:#1b1b1b;border-radius:6px}
.traits li{min-height:66px;display:flex;align-items:center;justify-content:center;text-align:center;font-size:18px;line-height:29px;color:var(--muted);border-bottom:2px solid #262626;padding:0 20px}
.traits li.tall{min-height:100px}
.card{background:var(--card);border-radius:10px;padding:24px 28px}
.card h3{display:flex;align-items:center;gap:12px;color:var(--orange);font-size:17px;font-weight:600;margin-bottom:16px}
.card h3 svg{width:34px;height:34px;flex:none}
.card ul{list-style:none}
.card li{position:relative;padding-left:16px;font-size:16px;line-height:24px;color:#e6e6e6;margin-bottom:17px}
.card li::before{content:"";position:absolute;left:0;top:10px;width:5px;height:5px;border-radius:50%;background:#fff}
.card-compact li{font-size:15.5px;margin-bottom:4px}
.bar-orange{left:65px;top:2390px;width:405px;height:56px;background:linear-gradient(90deg,var(--orange),var(--orange-deep));font-size:23px}
.rules{left:70px;top:2476px;width:412px;font-size:19.5px;line-height:32px;padding-left:16px;color:#f0f0f0}
</style>
</head>
<body>
<section class="abs hero">
  <div class="abs illustration" role="img" aria-label="Pink cratered planet illustration at the top edge" style="left:540px;top:0;width:140px;height:40px;border-radius:0 0 14px 14px;background:linear-gradient(180deg,#8a2a9a,#4a1860)"></div>
  <p class="abs why">Why:<br>Live everyday with integrity and<br>produce an output id admire</p>
  <h1 class="abs title">THE YEAR OF "NO"</h1>
  <ul class="abs bullets">
    <li>Deep minimalism - remove EVERYTHING that can be removed.</li>
    <li>No coaching - unless I get upside or am generating content</li>
    <li>No travel for events - Travel ok (w/ Lena, see family, building my core community, meditation retreat)</li>
    <li>No random rabbit-holes of Chirpline, email subscriptions, etc..</li>
  </ul>
  <div class="abs bar bar-green">The Statements</div>
  <div class="abs statement" style="left:696px">What you can be you must be?</div>
  <div class="abs statement" style="left:906px">What would Walter Brandt do?</div>
</section>

<section class="abs stage"></section>

<div class="abs illustration" role="img" aria-label="Illustration of a rocket launching upward on a fiery trail" style="left:434px;top:746px;width:323px;height:1190px;background:linear-gradient(180deg,#3c3a66 0%,#6a3050 45%,#4a1e2a 75%,#1a1416 100%)"></div>

<div class="abs illustration" role="img" aria-label="Pink ringed planet illustration" style="left:1090px;top:1530px;width:110px;height:110px;background:linear-gradient(160deg,#e070b0,#8a2a70)"></div>
<div class="abs illustration" role="img" aria-label="Blue ringed planet illustration" style="left:0;top:2090px;width:110px;height:110px;background:linear-gradient(160deg,#6aa8ee,#2a50a0)"></div>
<div class="abs illustration" role="img" aria-label="Green planet illustration" style="left:1030px;top:3325px;width:150px;height:140px;border-radius:14px 14px 0 0;background:linear-gradient(160deg,#70d060,#1a7a3a)"></div>

<div class="abs bar bar-purple">To be someone I'd<br>fully admire</div>
<div class="abs people">
  <div class="person" style="top:43px"><div class="portrait" role="img" aria-label="Portrait photo of Corin Vale"></div><p class="person-name">Corin<br>Vale</p></div>
  <div class="person" style="top:287px"><div class="portrait" role="img" aria-label="Portrait photo of Darius Knox"></div><p class="person-name">Darius<br>Knox</p></div>
  <div class="person" style="top:531px"><div class="portrait" role="img" aria-label="Portrait photo of Leland Fisk"></div><p class="person-name">Leland<br>Fisk</p></div>
  <div class="person" style="top:775px"><div class="portrait" role="img" aria-label="Portrait photo of Tobin Marsh"></div><p class="person-name">Tobin<br>Marsh</p></div>
  <div class="person" style="top:1019px"><div class="portrait" role="img" aria-label="Portrait photo of Rowan Pike"></div><p class="person-name">Rowan<br>Pike</p></div>
</div>

<div class="abs bar bar-pink">Inspiring Persons</div>
<ul class="abs traits">
  <li>Impact</li><li>Fitness</li><li>Thought leader</li>
  <li class="tall">Financially Liberated &amp; successful</li>
  <li>Business where passion is</li><li>Amazing community</li><li>Great relationship</li>
</ul>

<div class="abs card" style="left:540px;top:1797px;width:278px;height:198px;padding:22px 22px">
  <h3 style="margin-bottom:12px"><svg viewBox="0 0 24 24"><circle cx="12" cy="4" r="3" fill="#f7931e"/><path d="M4 8h16v3h-5v11h-3v-6h0v6H9V11H4z" fill="#f7931e"/></svg>Personal Brand</h3>
  <ul><li style="font-size:15.5px;line-height:23px">Collectively over 500,000 across Chirpline, Workgrid, Vidstream, Loopclip &amp; Snapfeed 26 videos I'm very proud of</li></ul>
</div>

<div class="abs card" style="left:838px;top:1797px;width:302px;height:538px">
  <h3><svg viewBox="0 0 24 24"><path d="M12 21S3 14 3 8.5A4.5 4.5 0 0 1 12 6a4.5 4.5 0 0 1 9 2.5C21 14 12 21 12 21z" fill="#f7931e"/><path d="M5 12h4l2-3 2 5 2-2h4" stroke="#1c1c1c" stroke-width="1.6" fill="none"/></svg>Fitness</h3>
  <ul>
    <li>85kg, 10% bf</li><li>Follow blueprint!</li><li>Handstand 30 secs</li>
    <li>~2-3 meals per day cooked for me - clear nutrition plan</li>
    <li>90 day no alcohol challenge / transformation.</li>
    <li>Exercise 6 days a week</li>
    <li>Clear goals with KPIs broken down by quarter and measured on my wall in gym. (Same with friends).</li>
  </ul>
</div>

<div class="abs card" style="left:540px;top:2012px;width:278px;height:470px">
  <h3><svg viewBox="0 0 24 24"><path d="M2 20V6l5 5 5-7 5 7 5-5v14z" fill="#f7931e"/></svg>Deep Mineralisation</h3>
  <ul>
    <li>Remove as many objects as possible</li>
    <li>Close open loops in my brain Remove as many decisions as possible.</li>
    <li>Automate as much as possible - food, fitness, calendar</li>
    <li>Limit number of projects allowed</li>
    <li>Calendar sweep</li>
  </ul>
</div>

<div class="abs card" style="left:838px;top:2358px;width:302px;height:297px">
  <h3><svg viewBox="0 0 24 24" fill="#f7931e"><circle cx="7" cy="7" r="3"/><circle cx="17" cy="7" r="3"/><circle cx="4" cy="14" r="2.5"/><circle cx="20" cy="14" r="2.5"/><ellipse cx="12" cy="17" rx="5" ry="4"/></svg>Community</h3>
  <ul>
    <li>Hosting brunch every ~2 weeks</li><li>Hosting 4 retreats</li><li>2 Nothing spared's</li>
    <li>2 Just amazing humans Hosting ~4 big events</li>
  </ul>
</div>

<div class="abs card card-compact" style="left:540px;top:2504px;width:278px;height:136px;padding:22px 16px">
  <h3 style="justify-content:center;margin-bottom:14px">Spiritual</h3>
  <ul><li>Do one meditation retreat</li><li>Do one Tantra workshop</li></ul>
</div>
<svg class="abs" style="left:662px;top:2646px" width="34" height="30" viewBox="0 0 24 22" aria-hidden="true"><circle cx="12" cy="4" r="3" fill="#f7931e"/><path d="M12 8v7M5 13l7-3 7 3M3 19h18" stroke="#f7931e" stroke-width="2.4" fill="none"/></svg>

<div class="abs card" style="left:540px;top:2683px;width:278px;height:208px">
  <h3><svg viewBox="0 0 24 24"><path d="M12 21S3 14 3 8.5A4.5 4.5 0 0 1 12 6a4.5 4.5 0 0 1 9 2.5C21 14 12 21 12 21z" fill="#f7931e"/></svg>Love</h3>
  <ul><li>Plan a fun date with Lena monthly</li><li>Tantra exploration Relationship coach</li></ul>
</div>

<div class="abs card card-compact" style="left:838px;top:2703px;width:302px;height:202px">
  <h3><svg viewBox="0 0 24 24" fill="#f7931e"><path d="M12 3 1 9l11 6 9-5v6h2V9z"/><path d="M5 13v4c2 2 5 3 7 3s5-1 7-3v-4l-7 4z"/></svg>Skills</h3>
  <ul><li style="margin-bottom:0">Dutch lessons</li><li style="margin-bottom:0">Personal conversational</li><li style="margin-bottom:0">Swedish</li></ul>
</div>

<div class="abs card" style="left:540px;top:2929px;width:600px;height:254px">
  <h3><svg viewBox="0 0 24 24"><rect x="2" y="2" width="20" height="20" rx="3" fill="#f7931e"/><text x="12" y="18" text-anchor="middle" font-family="Poppins,sans-serif" font-weight="700" font-size="15" fill="#1c1c1c">$</text></svg>Income</h3>
  <ul>
    <li>Sold Loudhaus, NW +$XXmil</li>
    <li>Build ~$Xxxmil+ income with Loudhaus US, and minority purchase in cash-flowing assets</li>
    <li>Start personal brand agency and scale to $XXXk/mo+</li>
  </ul>
</div>

<div class="abs bar bar-orange">YEARLY RULES</div>
<ol class="abs rules">
  <li>No Vidstream, TV, Movies, Flixbox &amp; games unless in the company of friends</li>
  <li>No social media (possible exception tbd is unless working out by my self)</li>
  <li>Get Tessa to post weekly Snapfeed stories on all my channels</li>
  <li>Get Tessa to review message requests on snapfeed/chirpline</li>
  <li>No eating off plan unless in the company of 4 or more people</li>
  <li>No caffeine</li>
  <li>No alcohol</li>
  <li>No additional projects - Unless the TOTAL time involvement is &lt; 30 hours in 2023 and the</li>
  <li>business is mission driven. Don't even explore other ideas. You got plenty to work on and</li>
  <li>solve mate. And I must convince Joel &amp; Arlo its worthy of my time.</li>
  <li>Audiobooks before bed instead of podcasts</li>
  <li>Only allowed 3 books reading at a time.</li>
  <li>Build friend CRM, actively reach out to interesting people every month</li>
</ol>
</body>
</html>
```